Corporate Business Card Design Project

..Hi designers!
I have established a consultancy within strategic communnications, for which I need a business card design - I've seen some of the things you do in here, and they're great! I'll provide some information in the following:
Name: BriarLedger
Tagline: Guiding Dialogue
Service: Strategic communications consulting (primariy internal communication and optimizing): various organisations - e.g. SMEs, NGOs and NPOs - are offered an analysis of their current efforts and, on the basis of that, management consulting tailored their unique challenges and needs.
It's a sole proprietorship - for now! - but it's my plan to employ 5-20 persons over the years. Therefore the card should NOT symbolize a start-up, but communicate a well-established, serious consultancy. Hence, it should also apply to serious companies and organizations - think Veltra or Hollis Brant Group (both as sender and receiver) ;)
The design should accordingly have a formal, conservative, stylish, corporate, clean look! and ditto colors, eg. black, grey, white etc - corresponding to the logo. The only colour that can appear is the same orange contrast as in my logo (see attachement). Not too bold or dramatic fonds or letters.
I choose the double sided as I think it gives the most professional look: One side with name, titel, phone, e-mail - then a little space - and four additional lines for address.
This composition is if all information should be in the same "column" - feel free to provide suggestions with the address places elsewhere on the one side.
On the other side, I'm only thinkin' something with the logo.
I'd be happy to see different ideas re. the use of the orange contrast, placement of logo, etc.
I do not plan on changing the design of businees cards ever - as I think it is more serious keeping a concept and avoid rebranding - and I'm sure that you can deliver an ever-lasting logo for my company! Thanks :).
Let's play the rest by ear in the correspondance.
Target Market(s)
Executive level: CEOs, HR directors, communication managers/directors, business owners.
Industry/Entity Type
Management Consulting

```html
<!DOCTYPE html>
<html lang="en">
<head>
<meta charset="utf-8">
<title>BriarLedger – Business Card</title>
<link rel="stylesheet" href="https://fonts.googleapis.com/css2?family=Crimson+Text:wght@400;600&display=swap">
<style>
  :root {
    --paper: #ffffff;
    --ink: #141414;
    --text: #3a3a3a;
    --muted: #5a5a5a;
    --soft: #8a8a8a;
    --accent: #f0872a;
  }
  html, body {
    margin: 0;
    padding: 0;
    width: 1200px;
    height: 716px;
    overflow: hidden;
    background: var(--paper);
  }
  .card {
    position: relative;
    width: 1200px;
    height: 716px;
    background: var(--paper);
    font-family: "Crimson Text", "Palatino Linotype", Georgia, serif;
    color: var(--text);
  }
  .accent-rule {
    position: absolute;
    left: 1029px;
    top: 0;
    width: 4px;
    height: 714px;
    background: var(--accent);
  }
  .brand {
    position: absolute;
    left: 88px;
    top: 106px;
  }
  .brand-name {
    margin: 0;
    font-size: 60px;
    line-height: 1;
    font-weight: 400;
    color: var(--ink);
    letter-spacing: -0.5px;
  }
  .brand-tagline {
    margin: 2px 0 0 158px;
    font-size: 12px;
    line-height: 1;
    letter-spacing: 6.5px;
    color: var(--soft);
    white-space: nowrap;
  }
  .identity {
    position: absolute;
    left: 545px;
    top: 276px;
    width: 440px;
    text-align: center;
  }
  .person-name {
    margin: 0;
    font-size: 69px;
    line-height: 1;
    font-weight: 400;
    color: var(--ink);
  }
  .person-title {
    margin: 22px 0 0 90px;
    font-size: 27px;
    line-height: 1;
    color: var(--muted);
  }
  .contact, .offices {
    position: absolute;
    left: 82px;
    margin: 0;
    padding: 0;
    list-style: none;
    font-size: 22px;
    line-height: 27.2px;
    color: var(--text);
  }
  .contact { top: 376px; }
  .offices { top: 496px; }
  .contact .indent { padding-left: 79px; }
</style>
</head>
<body>
  <main class="card">
    <div class="accent-rule"></div>

    <header class="brand">
      <p class="brand-name">BriarLedger</p>
      <p class="brand-tagline">Guiding Dialogue</p>
    </header>

    <section class="identity">
      <h1 class="person-name">Daniel Hartley</h1>
      <p class="person-title">Consultant</p>
    </section>

    <ul class="contact">
      <li>Adress: Linden Avenue 72,</li>
      <li class="indent">4816 Fairhaven</li>
      <li>Phone:&nbsp; 5550142937</li>
      <li>E-mail: danielhartley@briarledger.com</li>
    </ul>

    <ul class="offices">
      <li>adress: Cedar Avenue 3415, Brookmere, TX</li>
      <li>adress: Aspen Avenue 2287, Pinecrest, CO</li>
      <li>adress: Birch Avenue 6031, Ashford, NY</li>
      <li>adress: Willow Street 18, Ridgeway, MT</li>
    </ul>
  </main>
</body>
</html>
```